KWR CONSTRUCTION CO POSTCARD DESIGN

I was thinking of making a postcard for mailings by printmeadow and or by me dropping off at homes . I guess it would be used as a mailing post card and or flyer . I have had sketch harbor design my buisnes cards . The buisness card design is a different version from my signage on trucks because of space . I have a logo design . thyat i can upload . I like silver for back ground and black for logo and letters with glossy finish . I would like to have the KWR with a back drop to give it depth , it would be the same color as windows .

The file i submitted ha a design with red letters , this design is more detailed than the other and should be used . The colors should be black on a silver card glossy . The windows and maybe give the letters depth with a backdrop outline . I want to let home owners know that they can always call for consultation and and repairs or maintenance for their home .

Target Market(s)

home owners

Industry/Entity Type

Construction

Font styles to use
Other font styles liked:
• The same font as used in the picture of the sign i uploaded

Requirements
Must have
• HOME IMPROVEMENTS , MAINTENANCE AND REPAIRS , CARPENTRY , TILE PAINTING ECT

```html
<!DOCTYPE html>
<html lang="en">
<head>
<meta charset="utf-8">
<title>KWR Construction Co. – Postcard</title>
<link href="https://fonts.googleapis.com/css2?family=Jost:wght@400;700&family=Roboto+Condensed:ital,wght@1,700&display=swap" rel="stylesheet">
<style>
  :root {
    --stage: #bdbdbd;
    --ink: #000000;
    --paper: #ffffff;
    --silver-light: #e4e4e4;
    --silver-mid: #b2b0b1;
    --silver-dark: #a7a5a6;
    --guide: #b9b9b9;
    --logo-tile: #9a9a9a;
  }
  * { margin: 0; padding: 0; box-sizing: border-box; }
  html, body { width: 1200px; height: 649px; overflow: hidden; }
  body { background: var(--stage); font-family: "Jost", sans-serif; position: relative; }

  .card { position: absolute; top: 38px; width: 546px; height: 434px; }

  /* Front */
  .card-front { left: 50px; background: var(--ink); }
  .front-panel {
    position: absolute; left: 12px; top: 12px; width: 522px; height: 368px;
    background: radial-gradient(ellipse at 28% 55%, var(--silver-light) 0%, var(--silver-mid) 55%, var(--silver-dark) 100%);
  }
  .front-headline {
    position: absolute; left: 0; right: 0; top: 16px;
    text-align: center; font-weight: 700; font-size: 42px; line-height: 40px;
    color: var(--ink); letter-spacing: -0.3px;
  }
  .brand { position: absolute; display: flex; align-items: center; gap: 10px; }
  .brand-square { background: var(--logo-tile); flex: none; }
  .brand-name { font-weight: 700; color: var(--ink); line-height: 1; }
  .front-brand { left: 14px; top: 200px; }
  .front-brand .brand-square { width: 60px; height: 60px; }
  .front-brand .brand-name { font-size: 38px; }
  .front-brand .brand-name small { display: block; font-size: 15px; letter-spacing: 1.5px; margin-top: 6px; }

  .contact { position: absolute; color: var(--ink); }
  .web { font-family: "Roboto Condensed", sans-serif; font-style: italic; font-weight: 700; }
  .phone { font-weight: 700; letter-spacing: 1px; }
  .address { font-weight: 700; letter-spacing: 0.4px; }
  .front-contact { left: 268px; top: 264px; }
  .front-contact .web { font-size: 27px; line-height: 32px; }
  .front-contact .phone { font-size: 32px; line-height: 38px; margin-top: 8px; }
  .front-contact .address { font-size: 12.5px; line-height: 14px; margin-left: -4px; }

  .services {
    position: absolute; left: 0; right: 0; top: 394px;
    text-align: center; color: var(--paper);
    font-family: "Roboto Condensed", sans-serif; font-style: italic; font-weight: 700;
    font-size: 15.5px; letter-spacing: 0.2px;
  }

  /* Back */
  .card-back { left: 618px; background: var(--paper); }
  .back-brand { left: 20px; top: 24px; flex-direction: column; align-items: flex-start; gap: 6px; width: 120px; }
  .back-brand .brand-square { width: 38px; height: 38px; }
  .back-brand .brand-name { font-size: 24px; }
  .back-brand .brand-name small { display: block; font-size: 9px; letter-spacing: 1px; margin-top: 3px; }
  .back-contact { left: 174px; top: 38px; }
  .back-contact .web { font-size: 21px; line-height: 24px; }
  .back-contact .phone { font-size: 24px; line-height: 28px; margin-top: 4px; }
  .back-contact .address { font-size: 9.5px; line-height: 11px; margin-left: -3px; }

  .postage-zone {
    position: absolute; left: 457px; top: 18px; width: 71px; height: 78px;
    border: 1.5px solid var(--guide); color: var(--guide);
    font-size: 14px; line-height: 19px; text-align: center; padding-top: 10px;
  }
  .back-headline {
    position: absolute; left: 20px; top: 139px;
    font-weight: 700; font-size: 31px; line-height: 30px; color: var(--ink);
  }
  .guide-label { position: absolute; color: var(--guide); font-size: 13px; white-space: nowrap; transform: translateX(-50%); }
  .guide-mailing { left: 402px; top: 241px; font-size: 14px; }
  .guide-noaddress { left: 143px; top: 322px; }
  .guide-barcode { left: 274px; top: 404px; font-size: 14px; }
</style>
</head>
<body>
  <section class="card card-front" aria-label="Postcard front">
    <div class="front-panel">
      <h1 class="front-headline">Call for consultation,<br>repairs or<br>maintenance services.</h1>
      <div class="brand front-brand">
        <span class="brand-square"></span>
        <span class="brand-name">KWR<small>CONSTRUCTION CO.</small></span>
      </div>
      <div class="contact front-contact">
        <div class="web">kwrbuildco.com</div>
        <div class="phone">555 014 2288</div>
        <div class="address">12 Linden Row Ashford MA. 02199</div>
      </div>
    </div>
    <p class="services">HOME IMPROVEMENTS , MAINTENANCE &amp; REPAIRS , CARPENTRY , TILE PAINTING ECT</p>
  </section>

  <section class="card card-back" aria-label="Postcard back">
    <div class="brand back-brand">
      <span class="brand-square"></span>
      <span class="brand-name">KWR<small>CONSTRUCTION CO.</small></span>
    </div>
    <div class="contact back-contact">
      <div class="web">kwrbuildco.com</div>
      <div class="phone">555 014 2288</div>
      <div class="address">12 Linden Row Ashford MA. 02199</div>
    </div>
    <div class="postage-zone">Postage<br>Clear<br>Zone</div>
    <h2 class="back-headline">Call for<br>consultation,<br>repairs or<br>maintenance<br>services.</h2>
    <span class="guide-label guide-mailing">Mailing address Area</span>
    <span class="guide-label guide-noaddress">No Address in this area</span>
    <span class="guide-label guide-barcode">Barcode Area</span>
  </section>
</body>
</html>
```